Post card for landscape service

Velbrin Estate Management**FEATURED SERVICE*** Weekly Lawn mowing service starting at $15/ cutting ****other services****landscape servicespring and fall clean uplawn and flowerbed care (pest and weed control)fertilizing plantingand moreCall for a Free estimate!!10% off first months service with signed contract

Please make double sided ( a front and a back)

Target Market(s)

home owners

Industry/Entity Type

Landscape

Requirements
Must have
• please feture the weekly lawn mowing service and then list the other sevices
• contact info... can be found on business card that was uploaded.
• must say residential services
Should not have
• please dont list reo management

```html
<!DOCTYPE html>
<html lang="en">
<head>
<meta charset="utf-8">
<title>Velbrin Estate Management – Postcard</title>
<link href="https://fonts.googleapis.com/css2?family=Oswald:wght@500;600&family=Roboto+Condensed:wght@400;700&family=Montserrat:wght@500;600;700&display=swap" rel="stylesheet">
<style>
  :root{
    --bg:#e9e6e1;
    --paper:#ffffff;
    --ink:#151515;
    --green-dark:#137a35;
    --green:#1f8f3e;
    --green-mid:#2aa046;
    --green-light:#6cc07a;
    --yellow:#f3f08a;
    --text-grey:#333333;
    --line:#bdbdbd;
  }
  *{box-sizing:border-box;margin:0;padding:0}
  html,body{width:1200px;height:1000px;overflow:hidden;background:var(--bg)}
  .canvas{position:relative;width:1200px;height:1000px}
  .card{position:absolute;background:var(--paper);overflow:hidden;box-shadow:0 3px 10px rgba(0,0,0,.25)}

  /* FRONT */
  .card-front{left:78px;top:28px;width:645px;height:463px}
  .front-brand{position:absolute;left:28px;top:22px;font-family:'Oswald',sans-serif;font-weight:600;color:var(--ink);line-height:1}
  .brand-name{font-size:70px;letter-spacing:-1px;display:block}
  .brand-tag{font-size:24px;display:block;margin-top:3px;letter-spacing:-.2px}
  .front-contact{position:absolute;right:40px;top:42px;text-align:center;font-family:'Montserrat',sans-serif}
  .contact-segment{font-size:16px;font-weight:700;color:var(--green-dark);letter-spacing:.2px}
  .contact-phone{font-size:36px;font-weight:600;color:var(--ink);line-height:1.05;letter-spacing:-.5px}
  .contact-cta{font-size:14.5px;font-weight:500;color:var(--green-dark);letter-spacing:.6px;margin-top:2px}

  .front-photo{position:absolute;left:270px;top:147px;width:375px;height:316px;
    background:linear-gradient(180deg,#2f5a22 0%,#5b8f2d 18%,#4f9a2a 32%,#3f8d23 60%,#2f7a1d 100%)}
  .front-panel{position:absolute;left:0;top:147px;width:340px;height:316px}
  .front-panel svg{position:absolute;inset:0}
  .feature-title{position:absolute;left:27px;top:10px;font-family:'Oswald',sans-serif;font-weight:500;font-size:25px;line-height:1.1;color:#fff}
  .feature-price{position:absolute;left:27px;top:75px;font-family:'Oswald',sans-serif;font-weight:500;color:var(--yellow);line-height:1}
  .price-lead{font-size:21px;display:block}
  .price-amount{font-size:42px;display:block;margin-top:4px}
  .other-services{position:absolute;left:30px;top:163px;font-family:'Roboto Condensed',sans-serif;color:#fff}
  .other-title{font-family:'Oswald',sans-serif;font-weight:500;font-size:20px;margin-bottom:3px}
  .service-list{list-style:none;font-size:16px;line-height:1.35}
  .service-list li{position:relative;padding-left:17px}
  .service-list li svg{position:absolute;left:0;top:5px}
  .service-list .sub{display:block}
  .service-list li + li{margin-top:1px}

  /* BACK */
  .card-back{left:508px;top:506px;width:648px;height:465px}
  .back-photo{position:absolute;left:0;top:0;width:345px;height:166px;
    background:linear-gradient(180deg,#6f5a4a 0%,#8d7462 30%,#3d6e2a 55%,#5ea53a 80%,#4a9530 100%)}
  .back-curve{position:absolute;inset:0}
  .stamp{position:absolute;left:526px;top:19px;width:101px;height:111px;border:1px solid var(--line)}
  .address-line{position:absolute;left:377px;width:250px;border-top:1px solid var(--line)}
  .back-intro{position:absolute;left:21px;top:180px;width:285px;font-family:'Roboto Condensed',sans-serif;font-weight:700;font-size:11px;line-height:1.45;color:var(--ink)}
  .back-intro .intro-name{color:var(--green-dark)}
  .offer-ribbon{position:absolute;left:20px;top:253px;width:300px;height:46px;background:var(--green-dark);border-radius:8px 0 0 8px}
  .offer-text{position:absolute;left:120px;top:258px;font-family:'Roboto Condensed',sans-serif;font-size:17px;line-height:1.2;color:#fff;letter-spacing:.2px}
  .offer-badge{position:absolute;left:27px;top:247px;width:72px;height:72px;border-radius:50%;background:var(--green-light);border:3px solid #fff;box-shadow:0 0 0 2px var(--green-light);
    display:flex;flex-direction:column;align-items:center;justify-content:center;font-family:'Oswald',sans-serif;font-weight:600;color:#fff;line-height:.95}
  .offer-badge .pct{font-size:24px}
  .offer-badge .off{font-size:22px}
  .back-brand{position:absolute;left:0;width:350px;top:318px;text-align:center;font-family:'Oswald',sans-serif;font-weight:600;color:var(--ink);line-height:1}
  .back-brand .brand-name{font-size:48px;letter-spacing:-1px}
  .back-brand .brand-tag{font-size:16px;margin-top:2px}
  .back-contact{position:absolute;left:0;width:350px;top:390px;text-align:center;font-family:'Montserrat',sans-serif;color:var(--text-grey)}
  .back-phone{font-size:20px;font-weight:600;color:var(--green-dark);display:flex;align-items:center;justify-content:center;gap:5px}
  .back-line{font-size:12px;font-weight:500;margin-top:3px}
</style>
</head>
<body>
<div class="canvas">

  <section class="card card-front" aria-label="Postcard front">
    <div class="front-brand">
      <span class="brand-name">VELBRIN</span>
      <span class="brand-tag">ESTATE MANAGEMENT</span>
    </div>
    <div class="front-contact">
      <div class="contact-segment">COMMERCIAL &amp; RESIDENTIAL</div>
      <div class="contact-phone">555-014-2290</div>
      <div class="contact-cta">CALL FOR A FREE ESTIMATE!!</div>
    </div>

    <div class="front-photo" role="img" aria-label="Photo of a worker on a red ride-on mower cutting a striped green lawn with flowerbeds behind"></div>

    <div class="front-panel">
      <svg width="340" height="316" viewBox="0 0 340 316" aria-hidden="true">
        <path d="M0 0 H300 C285 60 270 110 290 180 C305 235 300 280 290 316 H0 Z" fill="var(--green-light)"/>
        <path d="M0 0 H288 C272 60 258 110 276 180 C290 235 286 280 276 316 H0 Z" fill="var(--green-dark)"/>
        <path d="M0 72 H266 C263 100 262 125 264 152 H0 Z" fill="var(--green-mid)"/>
      </svg>
      <div class="feature-title">WEEKLY LAWN<br>MOWING SERVICE</div>
      <div class="feature-price">
        <span class="price-lead">starting at</span>
        <span class="price-amount">$15/Cutting</span>
      </div>
      <div class="other-services">
        <div class="other-title">Other Services</div>
        <ul class="service-list">
          <li><svg width="12" height="12" viewBox="0 0 12 12"><rect x=".5" y=".5" width="11" height="11" fill="none" stroke="#fff"/><path d="M2.5 6 L5 8.5 L10 2" fill="none" stroke="#fff" stroke-width="1.6"/></svg>Landscape Service</li>
          <li><svg width="12" height="12" viewBox="0 0 12 12"><rect x=".5" y=".5" width="11" height="11" fill="none" stroke="#fff"/><path d="M2.5 6 L5 8.5 L10 2" fill="none" stroke="#fff" stroke-width="1.6"/></svg>Spring &amp; Fall Cleanups</li>
          <li><svg width="12" height="12" viewBox="0 0 12 12"><rect x=".5" y=".5" width="11" height="11" fill="none" stroke="#fff"/><path d="M2.5 6 L5 8.5 L10 2" fill="none" stroke="#fff" stroke-width="1.6"/></svg>Lawn And Flowerbed Care<span class="sub">(Pest And Weed Control)</span></li>
          <li><svg width="12" height="12" viewBox="0 0 12 12"><rect x=".5" y=".5" width="11" height="11" fill="none" stroke="#fff"/><path d="M2.5 6 L5 8.5 L10 2" fill="none" stroke="#fff" stroke-width="1.6"/></svg>Fertilizing Planting and More</li>
        </ul>
      </div>
    </div>
  </section>

  <section class="card card-back" aria-label="Postcard back">
    <div class="back-photo" role="img" aria-label="Photo of a brick colonial house with trimmed hedges, a green lawn and a sprinkler"></div>
    <svg class="back-curve" width="648" height="465" viewBox="0 0 648 465" aria-hidden="true">
      <path d="M345 0 C395 70 380 170 360 250 C345 320 338 400 338 465" fill="none" stroke="var(--green-dark)" stroke-width="16"/>
      <path d="M358 0 H378 C412 80 395 180 376 255 C360 325 354 400 354 465 H346 C346 400 352 320 368 250 C386 170 398 80 358 0 Z" fill="var(--green)"/>
      <path d="M337 0 V166 H0" fill="none" stroke="#111" stroke-width="2" stroke-dasharray="0"/>
    </svg>
    <div class="stamp"></div>
    <div class="address-line" style="top:231px"></div>
    <div class="address-line" style="top:303px"></div>

    <p class="back-intro"><span class="intro-name">Velbrin Estate Management</span> will help you manage your properties with services ranging from landscaping, pest control, snow removal and more.</p>

    <div class="offer-ribbon"></div>
    <div class="offer-text">FIRST MONTHS SERVICE<br>WITH SIGNED CONTRACT</div>
    <div class="offer-badge"><span class="pct">10%</span><span class="off">OFF</span></div>

    <div class="back-brand">
      <span class="brand-name">VELBRIN</span>
      <span class="brand-tag">ESTATE MANAGEMENT</span>
    </div>
    <div class="back-contact">
      <div class="back-phone">
        <svg width="15" height="15" viewBox="0 0 16 16" aria-hidden="true"><circle cx="8" cy="8" r="8" fill="var(--ink)"/><path d="M5.2 3.8 L6.6 5.6 L5.8 6.6 C6.4 8 7.8 9.4 9.4 10.2 L10.4 9.4 L12.2 10.8 L11.3 12.2 C8 12 4 8 3.8 4.7 Z" fill="#fff"/></svg>
        555-014-2290
      </div>
      <div class="back-line">PO Box 418 Harwell Glen, NJ 07999</div>
      <div class="back-line">velbrinestate@mailnest.com</div>
    </div>
  </section>

</div>
</body>
</html>
```